Premium Honey Fusions need a label design. 5 awesome blends (see below)

We need a label design for a line of honey. Brand is an existing brand called MELVORIK. www.melvorikusa.example
MELVORIK is a line of juices. The honey line is an extension of the MELVORIK juice line.
Blends are:
Honey Cinnamon
Honey Saffron
Honey Ginger
Honey Herbs
Honey Wild Flower
PRODUCT FROM INDIA
We need a label design for a line of honey. Brand is an existing brand called MELVORIK.
See www.melvorikusa.example
We would like to see label designs that:
-are easy to read, clean
-"Honey Cinnamon”, etc... should be prominent, as it will be what will set us apart.
-use colors that communicate "premium honey"
-premium
-unique
-healthy/good for you
-We need a “Help us save the bees” type message on the logo. We will give % of profit from sale of honey to go towards saving the bees.
The final design should communicate :
-healthy
-DELICIOUS!!!! (it is!)
-premium
-unique
-exotic
Glass bottle is square (see pics) and label has 3 sides:
Front panel
Side panel 1: will be nutritional, ingredients, UPC, etc
Side panel 2: a story about bees? about saffron, about cinnamon??
Target Market(s)
Hispanic and American markets.
Healthy conscious people.
Premium honey market
Look and feel

```html
<!DOCTYPE html>
<html lang="en">
<head>
<meta charset="utf-8">
<title>MELVORIK Premium Honey Labels</title>
<link rel="stylesheet" href="https://fonts.googleapis.com/css2?family=Arvo:wght@700&family=Caveat:wght@500;700&family=Montserrat:wght@500;700;800&display=swap">
<style>
  :root{
    --label-orange:#ee7623;
    --honey-yellow:#fbe43c;
    --paper:#ffffff;
    --ink:#1f1f1f;
    --swatch-lime:#a3c93a;
    --swatch-lemon:#f9ed3b;
    --swatch-gold:#fcc93a;
    --swatch-apricot:#f9a54a;
    --swatch-orange:#f07a22;
    --swatch-red:#e42a2a;
  }
  html,body{margin:0;padding:0;overflow:hidden;}
  body{width:1200px;height:1080px;background:var(--paper);position:relative;}
  .defs{position:absolute;width:0;height:0;}
  .label{position:absolute;width:496px;height:225px;}
  .label--cinnamon{left:79px;top:51px;}
  .label--saffron{left:79px;top:304px;}
  .label--ginger{left:79px;top:562px;}
  .label--wildflower{left:79px;top:821px;}
  .label--herbs{left:630px;top:51px;}
  .front-panel{position:absolute;left:701px;top:420px;width:360px;height:438px;}
  .accent-chip{position:absolute;left:498px;top:283px;width:42px;height:42px;background:var(--swatch-lemon);}
  .palette{position:absolute;left:740px;top:964px;display:flex;gap:6px;}
  .palette__swatch{width:43px;height:43px;}

  .band,.arch{fill:var(--label-orange);}
  .frame{fill:none;stroke:var(--paper);stroke-width:.8;}
  .rule{stroke:var(--paper);stroke-width:.6;}
  .brand{font-family:"Montserrat",sans-serif;font-weight:800;font-size:11px;fill:var(--honey-yellow);letter-spacing:.3px;}
  .premium{font-family:"Montserrat",sans-serif;font-weight:500;font-size:5.6px;fill:var(--paper);letter-spacing:1.2px;}
  .all-natural{font-family:"Caveat",cursive;font-weight:700;font-size:12px;fill:var(--paper);}
  .flavor{font-family:"Arvo",serif;font-weight:700;font-size:15px;fill:var(--honey-yellow);}
  .flavor--long{font-size:12.5px;}
  .tagline{font-family:"Caveat",cursive;font-weight:500;font-size:5.6px;fill:var(--paper);}
  .weight{font-family:"Montserrat",sans-serif;font-weight:700;font-size:6px;fill:var(--honey-yellow);}
  .bee-mark{fill:var(--honey-yellow);}
  .story{font-family:"Caveat",cursive;font-weight:500;font-size:4.4px;fill:var(--paper);}
  .nutrition-box{fill:var(--paper);stroke:var(--ink);stroke-width:.5;}
  .nutrition-title{font-family:"Arvo",serif;font-weight:700;font-size:6.4px;fill:var(--ink);}
  .nutrition-row{font-family:"Montserrat",sans-serif;font-weight:500;font-size:2.6px;fill:var(--ink);}
  .nutrition-rule{stroke:var(--ink);stroke-width:.35;}
  .nutrition-rule--heavy{stroke-width:1.6;}
</style>
</head>
<body>

<svg class="defs" aria-hidden="true">
  <defs>
    <g id="front">
      <path class="arch" d="M120,176 V68 A68,68 0 0 1 256,68 V176 Z"/>
      <path class="frame" d="M126,171 V68 A62,62 0 0 1 250,68 V171 Z"/>
      <text class="brand" x="188" y="26" text-anchor="middle">MELVORIK</text>
      <line class="rule" x1="146" y1="56" x2="166" y2="56"/>
      <text class="premium" x="188" y="58" text-anchor="middle">PREMIUM</text>
      <line class="rule" x1="210" y1="56" x2="230" y2="56"/>
      <text class="all-natural" x="188" y="80" text-anchor="middle">All Natural</text>
      <line class="rule" x1="146" y1="128" x2="230" y2="128"/>
      <circle class="bee-mark" cx="188" cy="139" r="4.5" role="img" aria-label="Small bee illustration"/>
      <text class="tagline" x="188" y="154" text-anchor="middle">Part of the profit goes to bees conservation efforts</text>
      <text class="weight" x="130" y="168">18 oz</text>
    </g>
    <g id="label-base">
      <rect class="band" x="0" y="52" width="388" height="98"/>
      <rect class="frame" x="4" y="56" width="380" height="90"/>
      <rect class="nutrition-box" x="6" y="58" width="64" height="72"/>
      <text class="nutrition-title" x="8" y="65">Nutrition Facts</text>
      <text class="nutrition-row" x="8" y="70">Serving Size 1 tbsp (21g)</text>
      <text class="nutrition-row" x="8" y="73.5">Servings Per Container 24</text>
      <line class="nutrition-rule nutrition-rule--heavy" x1="8" y1="76" x2="68" y2="76"/>
      <text class="nutrition-row" x="8" y="80">Calories 60</text>
      <line class="nutrition-rule" x1="8" y1="82" x2="68" y2="82"/>
      <text class="nutrition-row" x="48" y="85.5">% Daily Value</text>
      <line class="nutrition-rule" x1="8" y1="87" x2="68" y2="87"/>
      <text class="nutrition-row" x="8" y="90.5">Total Fat 0g</text><text class="nutrition-row" x="62" y="90.5">0%</text>
      <line class="nutrition-rule" x1="8" y1="92" x2="68" y2="92"/>
      <text class="nutrition-row" x="8" y="95.5">Sodium 0mg</text><text class="nutrition-row" x="62" y="95.5">0%</text>
      <line class="nutrition-rule" x1="8" y1="97" x2="68" y2="97"/>
      <text class="nutrition-row" x="8" y="100.5">Total Carb. 17g</text><text class="nutrition-row" x="62" y="100.5">6%</text>
      <line class="nutrition-rule" x1="8" y1="102" x2="68" y2="102"/>
      <text class="nutrition-row" x="11" y="105.5">Sugars 17g</text>
      <line class="nutrition-rule" x1="8" y1="107" x2="68" y2="107"/>
      <text class="nutrition-row" x="8" y="110.5">Protein 0g</text>
      <line class="nutrition-rule nutrition-rule--heavy" x1="8" y1="113" x2="68" y2="113"/>
      <text class="nutrition-row" x="8" y="118" textLength="58" lengthAdjust="spacingAndGlyphs">* Percent Daily Values are based on a</text>
      <text class="nutrition-row" x="8" y="121.5">2,000 calorie diet.</text>

      <text class="story" x="76" y="62">Ingredients: raw</text>
      <text class="story" x="76" y="67">honey, natural</text>
      <text class="story" x="76" y="72">spice blend.</text>
      <text class="story" x="76" y="77">Product from</text>
      <text class="story" x="76" y="82">India. Store in</text>
      <text class="story" x="76" y="87">a cool, dry</text>
      <text class="story" x="76" y="92">place. May</text>
      <text class="story" x="76" y="97">crystallize;</text>
      <text class="story" x="76" y="102">warm gently</text>
      <text class="story" x="76" y="107">to restore.</text>

      <text class="story" x="268" y="64" textLength="114" lengthAdjust="spacingAndGlyphs">This honey is gathered from wild blossoms</text>
      <text class="story" x="268" y="70" textLength="114" lengthAdjust="spacingAndGlyphs">in the hills of India, where bees roam free</text>
      <text class="story" x="268" y="76" textLength="114" lengthAdjust="spacingAndGlyphs">among spice gardens. Each jar is poured raw</text>
      <text class="story" x="268" y="82" textLength="114" lengthAdjust="spacingAndGlyphs">and unheated to keep the natural enzymes,</text>
      <text class="story" x="268" y="88" textLength="114" lengthAdjust="spacingAndGlyphs">aroma and golden colour the bees worked for.</text>
      <text class="story" x="268" y="94" textLength="114" lengthAdjust="spacingAndGlyphs">We blend it with whole spices and herbs for</text>
      <text class="story" x="268" y="100" textLength="114" lengthAdjust="spacingAndGlyphs">a taste that is rich, warm and gently exotic.</text>
      <text class="story" x="268" y="106">Enjoy it in tea, on toast or by the spoon.</text>
      <text class="story" x="268" y="116" textLength="114" lengthAdjust="spacingAndGlyphs">Part of every sale helps protect bee habitats</text>
      <text class="story" x="268" y="122" textLength="114" lengthAdjust="spacingAndGlyphs">and fund local conservation projects.</text>
      <text class="story" x="268" y="128">Thank you for helping us save the bees.</text>

      <use href="#front"/>
    </g>
  </defs>
</svg>

<svg class="label label--cinnamon" viewBox="0 0 388 176" role="group" aria-label="Honey Cinnamon label">
  <use href="#label-base"/>
  <text class="flavor" x="188" y="104" text-anchor="middle">Honey</text>
  <text class="flavor" x="188" y="121" text-anchor="middle">Cinnamon</text>
</svg>

<svg class="label label--saffron" viewBox="0 0 388 176" role="group" aria-label="Honey Saffron label">
  <use href="#label-base"/>
  <text class="flavor" x="188" y="104" text-anchor="middle">Honey</text>
  <text class="flavor" x="188" y="121" text-anchor="middle">Saffron</text>
</svg>

<svg class="label label--ginger" viewBox="0 0 388 176" role="group" aria-label="Honey Ginger label">
  <use href="#label-base"/>
  <text class="flavor" x="188" y="104" text-anchor="middle">Honey</text>
  <text class="flavor" x="188" y="121" text-anchor="middle">Ginger</text>
</svg>

<svg class="label label--wildflower" viewBox="0 0 388 176" role="group" aria-label="Honey Wild Flower label">
  <use href="#label-base"/>
  <text class="flavor" x="188" y="104" text-anchor="middle">Honey</text>
  <text class="flavor flavor--long" x="188" y="121" text-anchor="middle">Wild Flower</text>
</svg>

<svg class="label label--herbs" viewBox="0 0 388 176" role="group" aria-label="Honey Herbs label">
  <use href="#label-base"/>
  <text class="flavor" x="188" y="104" text-anchor="middle">Honey</text>
  <text class="flavor" x="188" y="121" text-anchor="middle">Herbs</text>
</svg>

<div class="accent-chip"></div>

<svg class="front-panel" viewBox="114 -2 148 180" role="group" aria-label="Honey Cinnamon front panel">
  <use href="#front"/>
  <text class="flavor" x="188" y="104" text-anchor="middle">Honey</text>
  <text class="flavor" x="188" y="121" text-anchor="middle">Cinnamon</text>
</svg>

<div class="palette">
  <div class="palette__swatch" style="background:var(--swatch-lime)"></div>
  <div class="palette__swatch" style="background:var(--swatch-lemon)"></div>
  <div class="palette__swatch" style="background:var(--swatch-gold)"></div>
  <div class="palette__swatch" style="background:var(--swatch-apricot)"></div>
  <div class="palette__swatch" style="background:var(--swatch-orange)"></div>
  <div class="palette__swatch" style="background:var(--swatch-red)"></div>
</div>

</body>
</html>
```